Verpackungsdesign für Fensterreiniger
Zielgruppe
Unsere Firma hat Produkte rund ums Fenster wie Fensterrahmenfolie, Rolladengurtfarbe und bald einen neuen Reiniger für vergilbte Fenster. Die Zielgruppe ist breit gefächert, von der Hausfrau bis zum Handwerker. Bei der Verpackung handelt es sich also um unseren Reiniger. Auf der Vorderseite sollte ein glänzender weißer Fensterrahmen sein. Die Beschriftung der Verpackung nehmen wir selbst vor. Bei der Datei handelt es sich um die Stanzskizze der Verpackung.
Aufgabenstellung
modisch dezent

```html
<!DOCTYPE html>
<html lang="de">
<head>
<meta charset="utf-8">
<title>Kunststofffenster Reiniger – Verpackung</title>
<link href="https://fonts.googleapis.com/css2?family=Jost:wght@300;400&display=swap" rel="stylesheet">
<style>
  :root {
    --bg: #e6e6e6;
    --gold: #8a7a44;
    --dark: #3e3e3e;
    --paper: #f1f1f1;
    --text-light: #ffffff;
    --text-muted: #d4d4d4;
    --text-gold: #d8c99a;
    --photo-light: #eef1f4;
    --photo-sky: #b9d3e6;
  }
  html, body {
    margin: 0;
    padding: 0;
    width: 775px;
    height: 1200px;
    overflow: hidden;
    background: var(--bg);
    font-family: "Jost", sans-serif;
  }
  .packaging {
    position: absolute;
    left: 100px;
    top: 50px;
    display: flex;
    height: 1100px;
  }
  .panel {
    display: flex;
    flex-direction: column;
    height: 100%;
  }
  .panel--front { width: 385px; }
  .panel--side  { width: 190px; }

  .band--gold  { background: var(--gold); }
  .band--dark  { background: var(--dark); }
  .band--paper { background: var(--paper); }

  .band--top-stripe  { height: 45px; }
  .band--dark-stripe { height: 50px; }
  .band--label-space { height: 185px; }

  .title-block {
    height: 210px;
    box-sizing: border-box;
    padding-top: 36px;
    text-align: center;
    color: var(--text-light);
  }
  .title-block__name {
    margin: 0;
    font-weight: 400;
    font-size: 39px;
    line-height: 1.15;
    letter-spacing: -0.5px;
    text-transform: uppercase;
  }
  .title-block__claim {
    margin: 24px 0 0;
    font-weight: 300;
    font-size: 20px;
  }

  .product-photo {
    height: 325px;
    background: linear-gradient(100deg, var(--photo-light) 0%, #f7f8fa 45%, var(--photo-sky) 100%);
  }

  .feature-row {
    height: 125px;
    display: flex;
    justify-content: space-around;
    align-items: center;
    padding: 0 22px;
  }
  .feature-row svg { display: block; }

  .front-footer {
    height: 160px;
    box-sizing: border-box;
    padding: 30px 30px 0;
    text-align: center;
    color: var(--text-light);
    font-size: 16px;
    line-height: 1.4;
    font-weight: 400;
  }

  .side-copy {
    box-sizing: border-box;
    padding: 34px 14px 0 16px;
    font-weight: 300;
    font-size: 14px;
    line-height: 1.65;
    margin: 0;
  }
  .side-copy p { margin: 0 0 28px; }
  .side-intro { height: 210px; color: var(--text-muted); }
  .side-details { height: 450px; color: var(--text-gold); padding-top: 40px; }
  .side-footer {
    height: 160px;
    box-sizing: border-box;
    padding-top: 62px;
    text-align: center;
    color: var(--text-light);
    font-size: 12px;
    font-weight: 300;
  }
</style>
</head>
<body>
  <main class="packaging">
    <section class="panel panel--front">
      <div class="band--gold band--top-stripe"></div>
      <div class="band--dark band--dark-stripe"></div>
      <div class="band--paper band--label-space"></div>
      <header class="band--dark title-block">
        <h1 class="title-block__name">Kunststofffenster<br>Reiniger</h1>
        <p class="title-block__claim">entfernt Vergilbungen an Fenster &amp; Rahmen</p>
      </header>
      <div class="product-photo" role="img" aria-label="Foto: glänzender weißer Kunststofffensterrahmen mit Griff vor blauem Himmel"></div>
      <div class="band--gold feature-row">
        <svg width="82" height="82" viewBox="0 0 82 82"><circle cx="41" cy="41" r="39" fill="none" stroke="#ffffff" stroke-width="1.5"/></svg>
        <svg width="82" height="82" viewBox="0 0 82 82"><circle cx="41" cy="41" r="39" fill="none" stroke="#ffffff" stroke-width="1.5"/></svg>
        <svg width="82" height="82" viewBox="0 0 82 82"><circle cx="41" cy="41" r="39" fill="none" stroke="#ffffff" stroke-width="1.5"/></svg>
      </div>
      <footer class="band--dark front-footer">
        Lorem ipsum dolor sit amet, consetetur sadipscing elitr, sed diam nonumy eirmod tempor invidunt ut labore et dolore magna aliquyam
      </footer>
    </section>

    <aside class="panel panel--side">
      <div class="band--gold band--top-stripe"></div>
      <div class="band--dark band--dark-stripe"></div>
      <div class="band--paper band--label-space"></div>
      <div class="band--dark side-copy side-intro">
        <p>Lorem ipsum dolor sit amet,<br>consetetur sadipscing elitr,<br>sed diam nonumy eirmod<br>tempor invidunt ut labore</p>
      </div>
      <div class="band--gold side-copy side-details">
        <p>Lorem ipsum dolor sit amet, consetetur sadipscing elitr, sed diam nonumy eirmod tempor invidunt ut labore et dolore magna aliquyam erat, sed diam voluptua.</p>
        <p>At vero eos et accusam et justo duo dolores et ea rebum.</p>
        <p>Stet clita kasd gubergren.</p>
      </div>
      <div class="band--dark side-footer">Lorem ipsum dolor sit amet</div>
    </aside>
  </main>
</body>
</html>
```